PLUM BUSINESS CARD

Need a business card and logo. The company name is PLUM (Coastal Society of Junior Equestrian Arts). It's a business that offers horseback riding lessons to young girls. Please put my name: Marlene Tobbitt and a place for email and phone number. I would like the card to look feminine and soft. I like script type lettering. I want the card to be white or ivory with black or gray and hot pink print. A horse head outline would be cool, something whimsical. Think teen girl who likes glamour. Also, I give western riding lessons. So I like faded out background Images of western saddles, cowgirls, horses with long hair, ropes, horses in sunset...mabe the word PLUM can be made out of a lasso rope?

Just updated my project with a little more detail

Target Market(s)

Young girls/ cowgirls, western riding

Industry/Entity Type

Horseback Riding

Font styles to use
Script

Colors
e34197

Requirements
Must have
• A logo of PLUM.
Must say Coastal Society of Junior Equestrian Arts
Colors are Pink and Black with an elegant, glamorous, feminine look.
Nice to have
• Could have a picture or outline of a horse

```html
<!DOCTYPE html>
<html lang="en">
<head>
<meta charset="UTF-8">
<title>PLUM Business Card</title>
<link rel="stylesheet" href="https://fonts.googleapis.com/css2?family=Kaushan+Script&family=Arimo:wght@400&display=swap">
<style>
  :root {
    --hot-pink: #e34197;
    --ink: #111111;
    --card-black: #161616;
    --card-black-soft: #262626;
    --paper: #ffffff;
    --backdrop: #cfcfcf;
    --contact-white: #ffffff;
  }
  html, body {
    margin: 0;
    padding: 0;
    width: 1200px;
    height: 900px;
    overflow: hidden;
    background: var(--backdrop);
  }
  .canvas {
    position: relative;
    width: 1200px;
    height: 900px;
    display: flex;
    align-items: center;
    justify-content: center;
  }
  .business-card {
    position: relative;
    width: 1000px;
    height: 580px;
    border-radius: 44px;
    overflow: hidden;
    background: var(--paper);
    box-shadow: 0 18px 40px rgba(0,0,0,0.25);
  }
  .logo-area {
    position: absolute;
    top: 0;
    left: 0;
    right: 0;
    height: 300px;
    display: flex;
    align-items: center;
    justify-content: center;
    gap: 26px;
  }
  .logo-name {
    font-family: "Kaushan Script", cursive;
    font-size: 190px;
    line-height: 1;
    color: var(--hot-pink);
    margin-top: 40px;
  }
  .logo-dot {
    width: 56px;
    height: 56px;
    border-radius: 50%;
    background: var(--hot-pink);
    margin-top: 40px;
  }
  .tagline-band {
    position: absolute;
    top: 300px;
    left: 0;
    right: 0;
    height: 42px;
    background: var(--hot-pink);
    display: flex;
    align-items: center;
    justify-content: center;
  }
  .tagline {
    font-family: "Kaushan Script", cursive;
    font-size: 30px;
    color: var(--ink);
    margin-top: -14px;
    white-space: nowrap;
  }
  .contact-panel {
    position: absolute;
    top: 342px;
    left: 0;
    right: 0;
    bottom: 0;
  }
  .contact-panel__texture {
    position: absolute;
    inset: 0;
    background: radial-gradient(ellipse at 50% 40%, var(--card-black-soft), var(--card-black) 75%);
  }
  .contact-details {
    position: relative;
    text-align: center;
    padding-top: 22px;
  }
  .holder-name {
    font-family: "Kaushan Script", cursive;
    font-size: 44px;
    color: var(--hot-pink);
    margin: 0;
    line-height: 1.1;
  }
  .contact-line {
    font-family: "Arimo", Arial, sans-serif;
    font-size: 36px;
    color: var(--contact-white);
    margin: 8px 0 0;
    line-height: 1.15;
  }
</style>
</head>
<body>
  <main class="canvas">
    <article class="business-card">
      <header class="logo-area">
        <span class="logo-name">PLUM</span>
        <span class="logo-dot"></span>
      </header>
      <div class="tagline-band">
        <span class="tagline">Coastal Society of Junior Equestrian Arts</span>
      </div>
      <section class="contact-panel">
        <div class="contact-panel__texture" role="img" aria-label="Black damask floral pattern background"></div>
        <div class="contact-details">
          <p class="holder-name">Marlene Tobbitt</p>
          <p class="contact-line">1742 306 518</p>
          <p class="contact-line">marlene@plumriding.com</p>
        </div>
      </section>
    </article>
  </main>
</body>
</html>
```